How do I determine which religion is correct?

This Infographic is part of the series "The Copper Lantern" found on my website www.brightmeadowpath.org.
This flow chart demonstrates a logical progression to determine which religion is correct based on historical factors and communication from the greatest conceivable being or God.

The main part of the sheet is the thought process starting with the question "How to I determine which religion is correct?"
The first question "Is the religion extant?" That is does the religion still exist. To the left you see no, these are defunct religions. To the right yes are religions that still exist and so pass on through the next question.

There are 5 main questions. The religions that get a no go into the "discarded bin" and the yes pass into the next question. Kind of like a funnel. Until the the end
The last question "Is there one eternal creator being?" Should be "Does the religion teach one eternal greatest conceivable being?" Also Hinduism should go to the "Yes" side not the no.

The 5 questions with the triangle have corresponding articles on the website. Also the right most questions in the flag-like box also have articles on the website and are associated with the question to the left. These articles and question provide more information.

This infographic is a quick reference to understand the thought process. I kind of like the idea of a funnel and waste basket, but I don't want to limit your creativity. I really like what you did on my last project, your design was beyond my best hopes.

If somehow these questions could be clickable links to the website that would be amazing.

```html
<!DOCTYPE html>
<html lang="en">
<head>
<meta charset="utf-8">
<title>How do I determine which religion is correct? — The Copper Lantern</title>
<link href="https://fonts.googleapis.com/css2?family=Montserrat:wght@500;600;700;800&display=swap" rel="stylesheet">
<style>
  :root {
    --teal: #17aeaa;
    --teal-dark: #0f6e68;
    --teal-deep: #0b5a55;
    --green: #4fdc33;
    --green-arrow: #5fdc2e;
    --red: #e0282e;
    --grey-col: #e5e5e5;
    --grey-panel: #ececec;
    --dots: #f2c14a;
    --ink: #222222;
    --white: #ffffff;
    --page: #ffffff;
  }
  * { box-sizing: border-box; margin: 0; padding: 0; }
  html, body {
    width: 1200px; height: 1200px; overflow: hidden;
    background: var(--page);
    font-family: "Montserrat", Arial, sans-serif;
  }
  .sheet {
    position: absolute; left: 30px; top: 197px;
    width: 858px; height: 606px;
    transform: scale(1.3287); transform-origin: 0 0;
    background: var(--white);
  }
  .abs { position: absolute; }
  a { color: inherit; text-decoration: none; }

  /* header */
  .header-main { left: 0; top: 0; width: 640px; height: 76px; background: var(--teal); }
  .header-side { left: 640px; top: 0; width: 218px; height: 76px; background: var(--green);
    display: flex; align-items: center; justify-content: center; text-align: center;
    color: var(--white); font-weight: 700; font-size: 19px; line-height: 1.1; }
  .brand { left: 18px; top: 27px; display: flex; align-items: center; gap: 8px;
    color: var(--white); font-weight: 600; font-size: 17px; }
  .brand-dot { width: 16px; height: 16px; border-radius: 50%; background: var(--white); }
  .title { left: 230px; top: 14px; width: 380px; text-align: center;
    color: var(--white); font-weight: 700; font-size: 18.5px; line-height: 1.17; }

  /* columns */
  .discard-col { left: 0; top: 76px; width: 110px; height: 530px; background: var(--grey-col); }
  .article-col { left: 640px; top: 76px; width: 218px; height: 530px; background: var(--grey-panel); }
  .divider { left: 110px; width: 530px; height: 0; border-top: 1.5px dotted var(--dots); }

  .discard-label { left: 0; width: 110px; text-align: center; color: var(--ink);
    font-weight: 700; font-size: 10.5px; line-height: 1.3; }

  /* question boxes */
  .question { left: 181px; width: 138px; height: 96px; background: var(--teal);
    clip-path: polygon(0 0, 100% 0, 100% 83%, 50% 100%, 0 83%);
    display: flex; align-items: center; justify-content: center; text-align: center;
    color: var(--white); font-weight: 700; font-size: 10.5px; line-height: 1.3; padding: 0 10px 14px; }
  .question.final { clip-path: none; padding-bottom: 0; }

  .arrow { width: 60px; height: 14px; }
  .answer { font-weight: 700; font-size: 9.5px; }
  .answer.no { color: var(--red); }
  .answer.yes { color: var(--green-arrow); }

  /* funnel */
  .funnel { left: 380px; top: 90px; width: 256px; height: 504px; }
  .funnel-text { left: 386px; width: 244px; text-align: center; color: var(--white);
    font-weight: 600; font-size: 10.5px; line-height: 1.3; }
  .verdict { left: 450px; top: 505px; width: 116px; height: 89px; background: var(--teal-deep);
    display: flex; flex-direction: column; align-items: center; justify-content: flex-end;
    padding-bottom: 7px; color: var(--white); font-weight: 600; font-size: 11.5px;
    line-height: 1.2; text-align: center; }
  .verdict svg { margin-bottom: 4px; }

  /* article cards */
  .card { left: 657px; width: 187px; background: var(--white); border: 1px solid var(--teal);
    color: var(--ink); font-weight: 500; font-size: 10px; line-height: 1.35; }
  .card b { font-weight: 700; }
  .card.tall { padding: 30px 50px 0 16px; }
  .card.tall .go { right: 6px; bottom: 6px; width: 27px; height: 27px; }
  .card.mid { display: flex; align-items: center; padding: 0 40px 0 8px; }
  .card.mid .go { right: 5px; top: 50%; margin-top: -13px; width: 26px; height: 26px; }
  .card.small { display: flex; align-items: center; padding: 0 26px 0 8px; font-size: 8px; line-height: 1.15; }
  .card.small .go { right: 3px; top: 50%; margin-top: -9px; width: 18px; height: 18px; }
  .go { position: absolute; border-radius: 50%; background: var(--teal);
    display: flex; align-items: center; justify-content: center; }
</style>
</head>
<body>
<main class="sheet">
  <header>
    <div class="abs header-main"></div>
    <div class="abs brand"><span class="brand-dot"></span>Lanternfold</div>
    <h1 class="abs title">HOW DO I DETERMINE<br>WHICH RELIGION IS CORRECT?</h1>
    <h2 class="abs header-side">THE COPPER<br>LANTERN</h2>
  </header>

  <div class="abs discard-col"></div>
  <div class="abs article-col"></div>

  <div class="abs divider" style="top:191px"></div>
  <div class="abs divider" style="top:293px"></div>
  <div class="abs divider" style="top:394px"></div>
  <div class="abs divider" style="top:496px"></div>

  <!-- funnel -->
  <svg class="abs funnel" viewBox="0 0 256 504" aria-hidden="true">
    <defs>
      <linearGradient id="funnelFill" x1="0" y1="0" x2="0" y2="1">
        <stop offset="0" stop-color="#52de3a"/>
        <stop offset="0.55" stop-color="#2cc57a"/>
        <stop offset="1" stop-color="#19a99e"/>
      </linearGradient>
    </defs>
    <polygon points="6,0 250,0 186,504 70,504" fill="url(#funnelFill)"/>
  </svg>

  <div class="abs funnel-text" style="top:104px">Christianity, Islam, Buddhism,<br>Hinduism, Judaism<br>Chinese Tradition, African Tradition,<br>Ethnic Religions, Sikhism, Jainism,<br>Zoroastrianism</div>
  <div class="abs funnel-text" style="top:214px">Buddhism, Hinduism, Judaism,<br>Jainism, Chinese Tradition,<br>African Tradition,<br>Ethnic Religions, Zoroastrianism</div>
  <div class="abs funnel-text" style="top:319px">Buddhism,<br>Hinduism, Judaism,<br>Jainism, Zoroastrianism</div>
  <div class="abs funnel-text" style="top:428px">Hinduism, Judaism,<br>Jainism</div>

  <div class="abs verdict">
    <svg width="38" height="42" viewBox="0 0 44 48" aria-hidden="true">
      <polygon points="22,2 41,35 3,35" fill="none" stroke="#fff" stroke-width="3.5"/>
      <polygon points="22,46 41,13 3,13" fill="none" stroke="#fff" stroke-width="3.5"/>
    </svg>
    HINDUISM,<br>JUDAISM
  </div>

  <svg width="0" height="0" style="position:absolute">
    <defs>
      <symbol id="arrow-left" viewBox="0 0 60 14"><rect x="10" y="5" width="50" height="4" fill="#e0282e"/><polygon points="0,7 13,0 13,14" fill="#e0282e"/></symbol>
      <symbol id="arrow-right" viewBox="0 0 60 14"><rect x="0" y="5" width="50" height="4" fill="#5fdc2e"/><polygon points="60,7 47,0 47,14" fill="#5fdc2e"/></symbol>
      <symbol id="pointer" viewBox="0 0 12 12"><path d="M2 1 L10 6 L6.4 6.8 L8.4 10.6 L7 11.3 L5 7.5 L2 9.8 Z" fill="#fff"/></symbol>
    </defs>
  </svg>

  <!-- row 1 -->
  <p class="abs discard-label" style="top:120px">Greek,<br>Roman, etc</p>
  <svg class="abs arrow" style="left:114px;top:125px"><use href="#arrow-left"/></svg>
  <span class="abs answer no" style="left:155px;top:136px">NO</span>
  <a class="abs question" style="top:90px" href="https://www.brightmeadowpath.org">IS THE<br>RELIGION<br>EXTANT?</a>
  <svg class="abs arrow" style="left:324px;top:123px"><use href="#arrow-right"/></svg>
  <span class="abs answer yes" style="left:326px;top:136px">YES</span>

  <!-- row 2 -->
  <p class="abs discard-label" style="top:216px">Christianity,<br>Islam,<br>Sikhism</p>
  <svg class="abs arrow" style="left:114px;top:227px"><use href="#arrow-left"/></svg>
  <span class="abs answer no" style="left:155px;top:238px">NO</span>
  <a class="abs question" style="top:192px" href="https://www.brightmeadowpath.org">IS THE<br>RELIGION OLD?<br>(BEFORE 500BC)</a>
  <svg class="abs arrow" style="left:324px;top:225px"><use href="#arrow-right"/></svg>
  <span class="abs answer yes" style="left:326px;top:238px">YES</span>

  <!-- row 3 -->
  <p class="abs discard-label" style="top:316px">Chinese<br>/African<br>Tradition,<br>Ethnic</p>
  <svg class="abs arrow" style="left:114px;top:328px"><use href="#arrow-left"/></svg>
  <span class="abs answer no" style="left:155px;top:340px">NO</span>
  <a class="abs question" style="top:294px" href="https://www.brightmeadowpath.org">IS THERE A<br>WRITTEN<br>TRADITION?</a>
  <svg class="abs arrow" style="left:324px;top:326px"><use href="#arrow-right"/></svg>
  <span class="abs answer yes" style="left:326px;top:340px">YES</span>

  <!-- row 4 -->
  <p class="abs discard-label" style="top:428px">Buddhism,<br>Zoroastrianism</p>
  <svg class="abs arrow" style="left:114px;top:430px"><use href="#arrow-left"/></svg>
  <span class="abs answer no" style="left:155px;top:442px">NO</span>
  <a class="abs question" style="top:396px" href="https://www.brightmeadowpath.org">DOES RELIGION<br>CLAIM &gt;1<br>COMMUNICATION?</a>
  <svg class="abs arrow" style="left:324px;top:430px"><use href="#arrow-right"/></svg>
  <span class="abs answer yes" style="left:326px;top:442px">YES</span>

  <!-- row 5 -->
  <p class="abs discard-label" style="top:543px">Jainism</p>
  <svg class="abs arrow" style="left:114px;top:536px"><use href="#arrow-left"/></svg>
  <span class="abs answer no" style="left:155px;top:548px">NO</span>
  <a class="abs question final" style="top:498px" href="https://www.brightmeadowpath.org">DOES THE RELIGION<br>TEACH ONE<br>ETERNAL GREATEST<br>CONCEIVABLE<br>BEING?</a>
  <svg class="abs arrow" style="left:324px;top:535px"><use href="#arrow-right"/></svg>
  <span class="abs answer yes" style="left:326px;top:548px">YES</span>

  <!-- article cards -->
  <a class="abs card tall" style="top:100px;height:86px" href="https://www.brightmeadowpath.org">Why must the<br>religion <b>still exist?</b><span class="go"><svg width="13" height="13"><use href="#pointer"/></svg></span></a>
  <a class="abs card tall" style="top:200px;height:86px" href="https://www.brightmeadowpath.org">Why must the<br>religion <b>be old?</b><span class="go"><svg width="13" height="13"><use href="#pointer"/></svg></span></a>
  <a class="abs card tall" style="top:300px;height:88px" href="https://www.brightmeadowpath.org">Why is a <b>written tradition</b> important?<span class="go"><svg width="13" height="13"><use href="#pointer"/></svg></span></a>
  <a class="abs card mid" style="top:400px;height:41px" href="https://www.brightmeadowpath.org"><span>Why does <b>2 or more communications matter</b>?</span><span class="go"><svg width="13" height="13"><use href="#pointer"/></svg></span></a>
  <a class="abs card mid" style="top:446px;height:42px" href="https://www.brightmeadowpath.org"><span>What is the <b>purpose</b><br>of communication?</span><span class="go"><svg width="13" height="13"><use href="#pointer"/></svg></span></a>
  <a class="abs card small" style="top:505px;height:25px" href="https://www.brightmeadowpath.org"><span>Why must there be a <b>first cause</b>?</span><span class="go"><svg width="9" height="9"><use href="#pointer"/></svg></span></a>
  <a class="abs card small" style="top:535px;height:27px" href="https://www.brightmeadowpath.org"><span>Why does <b>God have to be the creator</b>?</span><span class="go"><svg width="9" height="9"><use href="#pointer"/></svg></span></a>
  <a class="abs card small" style="top:567px;height:25px" href="https://www.brightmeadowpath.org"><span>Does something <b>have to be eternal</b>?</span><span class="go"><svg width="9" height="9"><use href="#pointer"/></svg></span></a>
</main>
</body>
</html>
```